Barefoot Bowls A5 Flyer

We require an A5 Flyer to promote Barefoot Bowls at Tallowby Lawn Club. We want to promote Barefoot Bowls as a fun activity for all ages, and various occasions. (Private Functions including Birthdays, Christmas, Bucks and Hens Parties, as well as Corporate Functions, and Fundraising / Charity groups). The design should be bright and colourful, and include images of coloured Barefoot Bowls, as well as a Jumping Castle (which we offer as an optional extra). Price is $10 per person for 2 hours, and includes Instructor and Equipment. Various Catering options available. For Bookings or Enquiries call Peter on 0472 316 554, or Sonia at the Club on 4917 2093. Club address is: 12-16 Hartwell Road, Tallowby NSW 2631.

```html
<!DOCTYPE html>
<html lang="en">
<head>
<meta charset="utf-8">
<title>Barefoot Bowls – Tallowby Lawn Club</title>
<link rel="stylesheet" href="https://fonts.googleapis.com/css2?family=Oswald:wght@500;700&family=Lato:ital,wght@0,400;0,700;1,700&display=swap">
<style>
  :root {
    --berry: #b8235a;
    --lime: #7cc242;
    --sun: #f4ee1a;
    --ink: #111111;
    --white: #ffffff;
    --cream: #fbe9b7;
  }
  * { margin: 0; padding: 0; box-sizing: border-box; }
  html, body { width: 900px; height: 1200px; overflow: hidden; background: #e9e9e9; }
  .flyer { position: relative; width: 900px; height: 1200px; overflow: hidden; font-family: "Lato", sans-serif; color: var(--ink); }
  .flyer-art { position: absolute; inset: 0; }
  .abs { position: absolute; }

  .title-barefoot { left: 68px; top: 402px; font: 700 78px/1 "Oswald", sans-serif; color: var(--berry); letter-spacing: 1px; }
  .title-barefoot .dark-o { color: var(--ink); }
  .title-bowls { left: 66px; top: 488px; font: 700 100px/1 "Oswald", sans-serif; color: var(--ink); letter-spacing: 1px; }
  .venue { left: 68px; top: 596px; font: 500 25px/1 "Oswald", sans-serif; color: var(--ink); }

  .pill { background: var(--ink); color: var(--white); font-style: italic; font-weight: 700; border-radius: 0 30px 30px 0; }
  .pill-functions { left: 0; top: 638px; width: 370px; height: 58px; padding: 6px 0 0 92px; font-size: 19px; line-height: 23px; }
  .pill-catering { left: 0; top: 868px; width: 498px; height: 52px; padding: 15px 0 0 52px; font-size: 19px; text-transform: uppercase; }

  .occasions { left: 84px; top: 708px; list-style: none; font-size: 20px; }
  .occasions li { display: flex; align-items: center; height: 32px; }
  .occasions svg { width: 18px; height: 18px; margin-right: 20px; }

  .address-label { left: 84px; top: 944px; font: 700 17px/1 "Oswald", sans-serif; color: var(--berry); }
  .address { left: 84px; top: 970px; font-size: 20px; }

  .price { left: 523px; width: 377px; text-align: center; color: var(--white); }
  .price-line { top: 738px; font: 700 19px/1 "Oswald", sans-serif; color: var(--ink); }
  .price-line .amount { font-size: 38px; color: var(--white); vertical-align: -4px; }
  .price-hours { top: 782px; font: 700 25px/1 "Oswald", sans-serif; color: var(--ink); }
  .price-includes { top: 816px; font-size: 18px; }
  .castle-1 { top: 844px; font: 700 26px/1 "Oswald", sans-serif; color: var(--ink); }
  .castle-2 { top: 874px; font: 700 36px/1 "Oswald", sans-serif; letter-spacing: 1px; }

  .enquiries { left: 548px; top: 928px; font: 500 23px/1 "Oswald", sans-serif; }
  .contact { left: 546px; top: 950px; font: 700 70px/1 "Oswald", sans-serif; letter-spacing: 3px; }
  .person { top: 1030px; font: 500 17px/21px "Oswald", sans-serif; }
  .person b { font-weight: 700; }
  .person .phone { color: var(--berry); font-weight: 700; }
  .person-peter { left: 548px; }
  .person-sonia { left: 726px; }
  .divider { left: 712px; top: 1034px; width: 2px; height: 54px; background: var(--ink); }
</style>
</head>
<body>
<main class="flyer">
  <svg class="flyer-art" viewBox="0 0 900 1200" width="900" height="1200">
    <defs>
      <linearGradient id="photoTone" x1="0" y1="0" x2="1" y2="1">
        <stop offset="0" stop-color="#c9c76a"/>
        <stop offset="0.45" stop-color="#8fa53a"/>
        <stop offset="0.7" stop-color="#2b2b22"/>
        <stop offset="1" stop-color="#b9b24a"/>
      </linearGradient>
      <radialGradient id="greenBurst" cx="300" cy="820" r="620" gradientUnits="userSpaceOnUse">
        <stop offset="0" stop-color="#f4ee1a"/>
        <stop offset="0.35" stop-color="#e4ea22"/>
        <stop offset="1" stop-color="#7cc242"/>
      </radialGradient>
      <radialGradient id="starFill" cx="676" cy="560" r="230" gradientUnits="userSpaceOnUse">
        <stop offset="0" stop-color="#fbe9b7"/>
        <stop offset="1" stop-color="#e8a3b5"/>
      </radialGradient>
      <linearGradient id="castleTone" x1="0" y1="0" x2="0" y2="1">
        <stop offset="0" stop-color="#3aa14a"/>
        <stop offset="0.6" stop-color="#2e7fc4"/>
        <stop offset="1" stop-color="#2a3f9e"/>
      </linearGradient>
      <linearGradient id="lawnBerry" x1="0" y1="0" x2="0" y2="1">
        <stop offset="0" stop-color="#c42e63"/>
        <stop offset="1" stop-color="#a61d51"/>
      </linearGradient>
    </defs>

    <rect x="0" y="0" width="900" height="470" fill="url(#photoTone)" role="img" aria-label="Photo of a black lawn bowl on the green beside a bare foot"/>

    <path d="M0,330 C200,300 420,330 560,410 C680,470 820,440 900,410 L900,1200 L0,1200 Z" fill="var(--berry)"/>
    <path d="M0,342 C200,312 420,342 560,422 C680,482 820,452 900,422 L900,1200 L0,1200 Z" fill="var(--white)"/>
    <path d="M0,352 C200,322 420,352 560,432 C680,492 820,462 900,432 L900,1200 L0,1200 Z" fill="var(--sun)"/>
    <path d="M0,360 C200,330 420,360 560,440 C680,500 820,470 900,440 L900,1200 L0,1200 Z" fill="url(#greenBurst)"/>

    <path d="M523,440 L900,440 L900,922 L548,922 Q523,922 523,897 Z" fill="var(--berry)"/>

    <polygon points="676,312 741,456 895,475 781,579 808,733 676,655 544,733 571,579 457,475 611,456" fill="var(--white)"/>
    <polygon points="676,330 736,464 880,481 773,577 799,718 676,645 553,718 579,577 472,481 616,464" fill="url(#starFill)"/>
    <rect x="572" y="478" width="210" height="172" rx="10" fill="url(#castleTone)" role="img" aria-label="Illustration of a tropical island jumping castle"/>

    <path d="M0,1062 C160,1015 330,1010 480,1060 C640,1110 800,1135 900,1140 L900,1200 L0,1200 Z" fill="var(--ink)"/>
    <path d="M0,1072 C160,1025 330,1020 480,1070 C640,1120 800,1145 900,1150 L900,1200 L0,1200 Z" fill="var(--white)"/>
    <path d="M0,1080 C160,1033 330,1028 480,1078 C640,1128 800,1153 900,1158 L900,1200 L0,1200 Z" fill="url(#lawnBerry)"/>
  </svg>

  <h1 class="abs title-barefoot">BAREF<span class="dark-o">OO</span>T</h1>
  <div class="abs title-bowls">BOWLS</div>
  <p class="abs venue">AT TALLOWBY LAWN CLUB</p>

  <p class="abs pill pill-functions">Book us for Private<br>Functions including:</p>
  <ul class="abs occasions">
    <li><svg viewBox="0 0 18 18"><circle cx="9" cy="9" r="7.5" fill="none" stroke="#111" stroke-width="1.6"/><path d="M7 5.5 L10.5 9 L7 12.5" fill="none" stroke="#111" stroke-width="1.8"/></svg>Birthdays</li>
    <li><svg viewBox="0 0 18 18"><circle cx="9" cy="9" r="7.5" fill="none" stroke="#111" stroke-width="1.6"/><path d="M7 5.5 L10.5 9 L7 12.5" fill="none" stroke="#111" stroke-width="1.8"/></svg>Christmas</li>
    <li><svg viewBox="0 0 18 18"><circle cx="9" cy="9" r="7.5" fill="none" stroke="#111" stroke-width="1.6"/><path d="M7 5.5 L10.5 9 L7 12.5" fill="none" stroke="#111" stroke-width="1.8"/></svg>Bucks and Hens Parties</li>
    <li><svg viewBox="0 0 18 18"><circle cx="9" cy="9" r="7.5" fill="none" stroke="#111" stroke-width="1.6"/><path d="M7 5.5 L10.5 9 L7 12.5" fill="none" stroke="#111" stroke-width="1.8"/></svg>Corporate Functions and</li>
    <li><svg viewBox="0 0 18 18"><circle cx="9" cy="9" r="7.5" fill="none" stroke="#111" stroke-width="1.6"/><path d="M7 5.5 L10.5 9 L7 12.5" fill="none" stroke="#111" stroke-width="1.8"/></svg>Fundraising / Charity groups</li>
  </ul>
  <p class="abs pill pill-catering">Various catering options available</p>

  <p class="abs address-label">CLUB ADDRESS :</p>
  <p class="abs address">12-16 Hartwell Road, Tallowby NSW 2631.</p>

  <p class="abs price price-line">PRICE IS <span class="amount">$10</span>/PERSON</p>
  <p class="abs price price-hours">FOR 2 HOURS</p>
  <p class="abs price price-includes">Includes Instructor and Equipment</p>
  <p class="abs price castle-1">JUMPING CASTLE</p>
  <p class="abs price castle-2">AVAILABLE</p>

  <p class="abs enquiries">BOOKINGS OR ENQUIRIES</p>
  <p class="abs contact">CONTACT</p>
  <p class="abs person person-peter"><b>PETER</b> ON<br><span class="phone">0472 316 554</span></p>
  <span class="abs divider"></span>
  <p class="abs person person-sonia"><b>SONIA</b><br>AT THE CLUB ON<br><span class="phone">4917 2093</span></p>
</main>
</body>
</html>
```